Painting services company needs a DL brochure about their services

We need a brochure describing our painting services including our logo and photos of work. The final design needs to be colourful, vibrant, and targeted to schools, aged care, commercial property maintenance clients.

```html
<!DOCTYPE html>
<html lang="en">
<head>
<meta charset="utf-8">
<title>Brightside Painters – DL Brochure Outside</title>
<link rel="stylesheet" href="https://fonts.googleapis.com/css2?family=Montserrat:wght@400;500;700;800;900&family=Open+Sans:wght@400;600&display=swap">
<style>
  :root {
    --navy: #1f2d8a;
    --navy-deep: #16206a;
    --yellow: #e6df63;
    --yellow-text: #cfc437;
    --lime: #c8d447;
    --white: #ffffff;
    --ink: #222222;
    --backdrop: #4a4a4a;
  }
  * { box-sizing: border-box; margin: 0; padding: 0; }
  html, body { width: 833px; height: 1200px; overflow: hidden; background: var(--backdrop); }
  .brochure {
    position: absolute; left: 20px; top: 291px; width: 794px; height: 617px;
    display: flex; background: var(--white);
    box-shadow: 0 10px 30px rgba(0,0,0,.35);
    font-family: "Open Sans", Arial, sans-serif; color: var(--ink);
  }
  .panel { position: relative; height: 100%; overflow: hidden; }
  .panel--about { width: 260px; }
  .panel--contact { width: 262px; }
  .panel--cover { width: 272px; }
  .site-band {
    position: absolute; left: 0; right: 0; bottom: 0; height: 34px;
    display: flex; align-items: center; justify-content: center;
    font-family: "Montserrat", sans-serif; font-size: 9.5px; letter-spacing: 1px;
    background: var(--lime); color: var(--navy-deep);
  }
  .site-band--navy { background: var(--navy-deep); color: var(--white); }

  /* About panel */
  .about-heading { position: absolute; left: 20px; top: 20px; width: 225px;
    font-family: "Montserrat", sans-serif; font-size: 17px; line-height: 1.16; }
  .about-heading .light { color: var(--yellow-text); font-weight: 500; display: block; }
  .about-heading .bold { color: var(--navy-deep); font-weight: 800; display: block; }
  .about-copy { position: absolute; left: 20px; top: 109px; width: 227px;
    font-size: 9.1px; line-height: 1.42; text-align: justify; }
  .work-photos { position: absolute; left: 21px; top: 225px; width: 226px; height: 210px; }
  .work-photos div { position: absolute; }
  .photo-a { left: 0; top: 0; width: 112px; height: 101px; background: linear-gradient(160deg,#d9d4c6,#8c7f66); }
  .photo-b { left: 116px; top: 0; width: 110px; height: 101px; background: linear-gradient(160deg,#bfc5c4,#6e6352); }
  .photo-c { left: 0; top: 105px; width: 78px; height: 105px; background: linear-gradient(180deg,#6b93d6,#b24a55); }
  .photo-d { left: 82px; top: 105px; width: 144px; height: 105px; background: linear-gradient(160deg,#d8c3a5,#8a4b35); }
  .attitude { position: absolute; left: 0; right: 0; top: 454px; text-align: center;
    font-family: "Montserrat", sans-serif; font-size: 15.5px; line-height: 1.27; color: var(--navy-deep); font-weight: 500; }
  .attitude .hl { color: var(--yellow-text); font-weight: 700; }
  .attitude .big { color: var(--yellow-text); font-weight: 800; font-size: 20px; }

  /* Contact panel */
  .intro-block { position: absolute; left: 0; top: 0; width: 100%; height: 323px; background: var(--yellow); }
  .intro-title { position: absolute; left: 0; right: 0; top: 24px; text-align: center;
    font-family: "Montserrat", sans-serif; font-weight: 900; font-size: 25px; line-height: 1.1; color: var(--white); }
  .intro-copy { position: absolute; left: 22px; right: 22px; top: 100px; text-align: center;
    font-size: 10px; line-height: 1.45; color: var(--ink); }
  .quote-button { position: absolute; left: 36px; top: 172px; width: 186px; height: 40px;
    background: var(--navy-deep); color: var(--yellow); border-right: 4px solid var(--navy);
    font-family: "Montserrat", sans-serif; font-weight: 700; font-size: 13.5px;
    display: flex; align-items: center; justify-content: center; }
  .site-photo { position: absolute; left: 38px; top: 242px; width: 176px; height: 176px; border-radius: 50%;
    border: 18px solid var(--navy); background: radial-gradient(circle at 45% 40%,#e6ecef,#8ea6be); }
  .touch-heading { position: absolute; left: 0; right: 0; top: 446px; text-align: center;
    font-family: "Montserrat", sans-serif; font-weight: 800; font-size: 16px; color: var(--navy-deep); }
  .touch-heading span { color: var(--yellow-text); }
  .contact-list { position: absolute; left: 34px; top: 477px; width: 206px; list-style: none; }
  .contact-list li { display: flex; align-items: center; gap: 9px; padding: 3px 0; border-bottom: 1px solid #e2df9a; font-size: 10px; line-height: 1.4; }
  .contact-list li:last-child { border-bottom: none; }
  .contact-list .phone { font-family: "Montserrat", sans-serif; font-weight: 700; font-size: 17px; color: var(--yellow-text); }
  .icon { width: 20px; height: 20px; flex: none; }

  /* Cover panel */
  .cover-title { position: absolute; left: 16px; top: 24px; font-family: "Montserrat", sans-serif;
    font-weight: 900; font-size: 26px; line-height: .98; color: var(--navy-deep); }
  .cover-title .yl { color: var(--yellow); }
  .cover-title .sm { font-size: 17.5px; }
  .cover-rule { position: absolute; left: 16px; top: 103px; width: 38px; height: 2px; background: var(--yellow); }
  .cover-sub { position: absolute; left: 16px; top: 110px; font-size: 13px; line-height: 1.25; color: var(--ink); }
  .cover-sub b { color: var(--navy-deep); font-weight: 600; }
  .brand-mark { position: absolute; left: 178px; top: 22px; width: 85px; height: 112px; background: var(--navy);
    display: flex; align-items: flex-end; padding: 0 8px 12px; }
  .brand-mark span { font-family: "Montserrat", sans-serif; font-weight: 700; font-size: 12px; line-height: 1.1; color: var(--white); }
  .hero-photo { position: absolute; left: -33px; top: 162px; width: 352px; height: 352px; border-radius: 50%;
    border: 24px solid var(--navy); background: radial-gradient(circle at 50% 45%,#eef1f4,#3b56b8 75%); }
  .cover-cta { position: absolute; left: 0; right: 0; top: 538px; text-align: center;
    font-family: "Montserrat", sans-serif; font-weight: 800; line-height: 1.2; }
  .cover-cta .a { color: var(--navy-deep); font-size: 15px; display: block; }
  .cover-cta .b { color: var(--yellow-text); font-size: 18px; display: block; }
</style>
</head>
<body>
<main class="brochure">
  <section class="panel panel--about">
    <h2 class="about-heading"><span class="light">WE ARE A<br>FAMILY-RUN BUSINESS</span><span class="bold">WITH OVER 40 YEARS' EXPERIENCE</span></h2>
    <p class="about-copy">We provide a full range of painting, decorating and protective coatings services through specialised divisions. This is the best way to guarantee that our clients are getting the best level of customer service possible from the enquiry and quotation to the provision of the right staff with the right skills and attitude to carry out the required preparation and application.</p>
    <div class="work-photos">
      <div class="photo-a" role="img" aria-label="Photo of a freshly painted hospital corridor"></div>
      <div class="photo-b" role="img" aria-label="Photo of a painted gym interior"></div>
      <div class="photo-c" role="img" aria-label="Photo of a painted commercial building exterior"></div>
      <div class="photo-d" role="img" aria-label="Photo of a painted retail store interior"></div>
    </div>
    <p class="attitude">REMEMBER,<span class="hl">WHEN YOU</span><br><span class="hl">NEED PAINTERS</span><br>FOR A COMMERCIAL<br>BUILDING WE ARE THE<br>PAINTERSWITH THE<br><span class="big">RIGHT ATTITUDE</span></p>
    <div class="site-band">www.brightsidepainters.com.au</div>
  </section>

  <section class="panel panel--contact">
    <div class="intro-block">
      <h2 class="intro-title">BRIGHTSIDE<br>PAINTERS</h2>
      <p class="intro-copy">Brightside Painters is a specialist commercial painting, decorating and protective coatings application company servicing all states of Australia</p>
      <div class="quote-button">Get a FAST QUOTE!</div>
    </div>
    <div class="site-photo" role="img" aria-label="Photo of painted industrial tanks on a site"></div>
    <h3 class="touch-heading"><span>GET</span> IN TOUCH</h3>
    <ul class="contact-list">
      <li><svg class="icon" viewBox="0 0 20 20"><circle cx="10" cy="10" r="10" fill="#1f2d8a"/><path d="M10 4.5a3.5 3.5 0 0 0-3.5 3.5c0 2.6 3.5 7 3.5 7s3.5-4.4 3.5-7A3.5 3.5 0 0 0 10 4.5z" fill="#e6df63"/><circle cx="10" cy="8" r="1.3" fill="#1f2d8a"/></svg><span>P.O. Box 410<br>Hillview, NSW 2000</span></li>
      <li><svg class="icon" viewBox="0 0 20 20"><circle cx="10" cy="10" r="10" fill="#1f2d8a"/><rect x="6.5" y="4.5" width="7" height="11" rx="1.3" fill="#e6df63"/><rect x="7.8" y="6" width="4.4" height="7" fill="#1f2d8a"/></svg><span class="phone">1300 555 019</span></li>
      <li><svg class="icon" viewBox="0 0 20 20"><circle cx="10" cy="10" r="10" fill="#1f2d8a"/><g fill="none" stroke="#e6df63" stroke-width="1.1"><circle cx="10" cy="10" r="5"/><ellipse cx="10" cy="10" rx="2.2" ry="5"/><path d="M5 10h10"/></g></svg><span>hello@brightsidepainters.com.au<br>www.brightsidepainters.com.au</span></li>
    </ul>
    <div class="site-band site-band--navy">www.brightsidepainters.com.au</div>
  </section>

  <section class="panel panel--cover">
    <h1 class="cover-title">FRIENDLY<br><span class="yl">PAINTING</span><br><span class="sm">CONTRACTORS</span></h1>
    <div class="cover-rule"></div>
    <p class="cover-sub">Commercial Painters<br>in <b>Australia</b></p>
    <div class="brand-mark"><span>Brightside<br>Painters</span></div>
    <div class="hero-photo" role="img" aria-label="Photo of painters pouring green paint from a tin"></div>
    <p class="cover-cta"><span class="a">CALL OR EMAIL US NOW</span><span class="b">TO GET A FAST QUOTE!</span></p>
    <div class="site-band">www.brightsidepainters.com.au</div>
  </section>
</main>
</body>
</html>
```